Bright Path Attorneys Billboard Design for Personal Injury Law Firm

Need a billboard design that we can use for different versions. 1400px X 400px jpeg or png
I have attached the logo and the attorney for the billboard. Attorney Marla Benning
Here is a link to our current website brightpathlegalgroup.example

HEADLINE: HIT BY A TRUCK?
SUBHEAD: NO FEE. BIG FIGHT.
877-GRANTLY

HEADLINE: ACCIDENT?
SUBHEAD: NO FEE, UNLESS WE WIN!
877-GRANTLY

HEADLINE: BIG TRUCK. BIG CASE.
SUBHEAD: YOU PAY $0 UPFRONT
877-GRANTLY

Target Market(s)

People in Car Accident

Industry/Entity Type

Personal Injury Attorneys

```html
<!DOCTYPE html>
<html lang="en">
<head>
<meta charset="utf-8">
<title>Bright Path Attorneys Billboard</title>
<link rel="stylesheet" href="https://fonts.googleapis.com/css2?family=League+Gothic&family=Oswald:wght@500;600&family=Oranienbaum&family=Poppins:wght@500&display=swap">
<style>
  :root {
    --board-black: #121212;
    --panel-grey: #2f2f31;
    --brand-yellow: #f7cf12;
    --band-white: #ffffff;
    --ink-black: #111111;
    --logo-grey: #6a6a6a;
    --page-bg: #e9e9ea;
  }
  * { margin: 0; padding: 0; box-sizing: border-box; }
  html, body {
    width: 1200px; height: 800px; overflow: hidden;
    background: var(--page-bg);
  }
  .billboard {
    position: absolute; left: 30px; top: 188px;
    width: 1140px; height: 423px;
    background: var(--board-black);
    overflow: hidden;
  }
  .headline {
    position: absolute; left: 20px; top: 34px;
    font-family: "League Gothic", "Oswald", sans-serif;
    font-size: 98px; line-height: 1;
    color: var(--brand-yellow);
    white-space: nowrap;
  }
  .subhead-band {
    position: absolute; left: 18px; top: 140px;
    width: 440px; height: 58px;
  }
  .subhead-text {
    position: absolute; left: 42px; top: 141px;
    font-family: "Oswald", sans-serif; font-weight: 500;
    font-size: 40px; line-height: 56px;
    color: var(--ink-black);
    white-space: nowrap;
  }
  .car-photo {
    position: absolute; left: 512px; top: 12px;
    width: 172px; height: 164px;
    background: linear-gradient(160deg, #5c5f66 0%, #3d3f44 55%, #222326 100%);
  }
  .title-band {
    position: absolute; left: 459px; top: 180px;
    width: 312px; height: 56px;
  }
  .title-text {
    position: absolute; left: 492px; top: 180px;
    font-family: "Oswald", sans-serif; font-weight: 500;
    font-size: 42px; line-height: 56px;
    color: var(--ink-black);
  }
  .attorney-name {
    position: absolute; left: 484px; top: 254px;
    font-family: "Oranienbaum", serif;
    font-size: 52px; line-height: 1;
    color: var(--band-white);
    white-space: nowrap;
  }
  .phone {
    position: absolute; left: 486px; top: 322px;
    display: flex; align-items: center; gap: 14px;
    font-family: "Oswald", sans-serif; font-weight: 600;
    font-size: 54px; line-height: 1;
    color: var(--brand-yellow);
    white-space: nowrap;
  }
  .phone svg { width: 22px; height: 26px; }
  .logo {
    position: absolute; left: 20px; top: 248px;
    display: flex; align-items: center; gap: 16px;
  }
  .logo-mark {
    width: 64px; height: 64px; border-radius: 50%;
    background: var(--logo-grey);
  }
  .logo-name {
    font-family: "Poppins", sans-serif; font-weight: 500;
    font-size: 34px; line-height: 1.05;
    color: var(--logo-grey);
  }
  .website {
    position: absolute; left: 22px; top: 340px;
    display: flex; align-items: center; gap: 10px;
    font-family: "Poppins", sans-serif; font-weight: 500;
    font-size: 25px; line-height: 1;
    color: var(--brand-yellow);
    white-space: nowrap;
  }
  .website svg { width: 22px; height: 26px; }
  .portrait-panel {
    position: absolute; right: 0; top: 0;
    width: 292px; height: 423px;
  }
</style>
</head>
<body>
  <div class="billboard">
    <div class="headline">HIT BY A TRUCK?</div>

    <svg class="subhead-band" viewBox="0 0 440 58" aria-hidden="true">
      <polygon points="0,8 420,0 440,58 0,58" fill="var(--band-white)"/>
    </svg>
    <div class="subhead-text">NO FEE. BIG FIGHT.</div>

    <div class="car-photo" role="img" aria-label="Photo of a car with a crushed front end after a collision"></div>

    <svg class="title-band" viewBox="0 0 312 56" aria-hidden="true">
      <polygon points="0,6 298,0 312,50 12,56" fill="var(--brand-yellow)"/>
    </svg>
    <div class="title-text">ATTORNEY</div>

    <div class="attorney-name">MARLA BENNING</div>

    <div class="phone">
      <svg viewBox="0 0 24 28" aria-hidden="true">
        <path d="M6 2 L10 2 L11 9 L8 11 Q10 17 15 20 L17 17 L23 18 L23 23 Q23 26 19 26 Q4 23 2 6 Q2 2 6 2 Z" fill="var(--band-white)"/>
      </svg>
      <span>877-GRANTLY</span>
    </div>

    <div class="logo">
      <div class="logo-mark"></div>
      <div class="logo-name">BRIGHT PATH<br>ATTORNEYS</div>
    </div>

    <div class="website">
      <svg viewBox="0 0 22 26" aria-hidden="true">
        <polygon points="2,2 2,22 7,17 11,25 14,23.5 10,16 17,16" fill="var(--band-white)"/>
      </svg>
      <span>brightpathlegalgroup.example</span>
    </div>

    <svg class="portrait-panel" viewBox="0 0 292 423" role="img" aria-label="Portrait photo of attorney Marla Benning in a navy blazer, arms crossed">
      <defs>
        <linearGradient id="portraitTone" x1="0" y1="0" x2="0" y2="1">
          <stop offset="0" stop-color="#3a3a3c"/>
          <stop offset="0.55" stop-color="#2f2f31"/>
          <stop offset="1" stop-color="#1e2436"/>
        </linearGradient>
      </defs>
      <polygon points="0,0 292,0 292,423 26,423" fill="url(#portraitTone)"/>
    </svg>
  </div>
</body>
</html>
```